Business Card Design Project

Business is web based; no retail location. Business card needs to direct potential customers to our website.

Target Market(s)

Parents, Adult Fans of Vantri

Industry/Entity Type

Retail

Requirements
Must have
• Email Address
Website Address
Should not have
• Telephone Number

```html
<!DOCTYPE html>
<html lang="en">
<head>
<meta charset="utf-8">
<title>Harbor Town Blocks – Business Card</title>
<link rel="stylesheet" href="https://fonts.googleapis.com/css2?family=Cinzel:wght@400;700&display=swap">
<style>
  :root {
    --page-bg: #f2f2f2;
    --card-red: #c72420;
    --card-mid: #6e1311;
    --card-dark: #140606;
    --swoosh-red: #e0342b;
    --step-line: #8a1e1a;
    --ink-light: #ffffff;
  }
  html, body {
    margin: 0;
    padding: 0;
    width: 1200px;
    height: 900px;
    overflow: hidden;
    background: var(--page-bg);
  }
  .stage {
    position: relative;
    width: 1200px;
    height: 900px;
  }
  .business-card {
    position: absolute;
    left: 146px;
    top: 191px;
    width: 907px;
    height: 518px;
    display: block;
  }
  .contact-text {
    font-family: "Cinzel", serif;
    font-weight: 400;
    fill: var(--ink-light);
  }
  .brand-name {
    font-family: "Cinzel", serif;
    font-weight: 700;
    fill: var(--ink-light);
  }
</style>
</head>
<body>
<main class="stage">
  <svg class="business-card" viewBox="0 0 623 356" xmlns="http://www.w3.org/2000/svg">
    <defs>
      <linearGradient id="card-surface" x1="0" y1="0" x2="1" y2="0">
        <stop offset="0" stop-color="var(--card-red)"/>
        <stop offset="0.45" stop-color="var(--card-mid)"/>
        <stop offset="1" stop-color="var(--card-dark)"/>
      </linearGradient>
      <linearGradient id="swoosh-fill" x1="0" y1="0" x2="1" y2="0">
        <stop offset="0" stop-color="var(--swoosh-red)"/>
        <stop offset="0.5" stop-color="var(--card-mid)"/>
        <stop offset="1" stop-color="var(--card-dark)"/>
      </linearGradient>
      <clipPath id="card-shape">
        <rect x="0" y="0" width="623" height="356" rx="12"/>
      </clipPath>
    </defs>

    <g clip-path="url(#card-shape)">
      <rect class="card-surface" x="0" y="0" width="623" height="356" fill="url(#card-surface)"/>

      <g class="step-lines" fill="none" stroke="var(--step-line)" stroke-width="1.5">
        <path d="M248,356 L310,10 L623,10"/>
        <path d="M302,356 L362,65 L623,65"/>
        <path d="M330,356 L378,118 L623,118"/>
        <path d="M368,356 L406,173 L623,173"/>
        <path d="M408,356 L436,228 L623,228"/>
        <path d="M448,356 L466,285 L623,285"/>
      </g>

      <path class="bottom-swoosh" d="M0,262 Q260,300 623,342 L623,356 L0,356 Z" fill="url(#swoosh-fill)"/>
      <path class="swoosh-edge" d="M0,262 Q260,300 623,342" fill="none" stroke="#ff5a48" stroke-opacity="0.35" stroke-width="1"/>
    </g>

    <g class="brand-mark">
      <text class="brand-name" x="140" y="170" font-size="34" text-anchor="middle">Harbor</text>
      <text class="brand-name" x="140" y="210" font-size="34" text-anchor="middle">Town</text>
      <text class="brand-name" x="140" y="250" font-size="34" text-anchor="middle">Blocks</text>
    </g>

    <text class="contact-text website" font-size="12" letter-spacing="3.2"
          transform="translate(316,42) rotate(100)">WWW.XXXXXXX.COM</text>

    <text class="contact-text email" x="352" y="50" font-size="12">XXXXXXXXXXXXXXX@GMAIL.COM</text>
  </svg>
</main>
</body>
</html>
```